2-Page Flyer for the Information Session about the Tranquil Venture Course

This is a flyer to announce/advertise an evening Information Session about the Tranquil Venture Course. This Program aims at mindfully rethinking and redesigning work (and life) for people who feel stuck or not entirely satisfied with their work and/or life (please see draft flyer attached for more details). This Program is property of Brightfold Joy, a company that uses a combination of Mindfulness, Design, and Entrepreneurship to help people achieve greater happiness (in their work and lives).
Updates

Target Market(s)

People who feel stuck or not entirely satisfied with their work and/or life (please see draft flyer attached for more details)

Font styles to use
Serif
Sans Serif

Colors
ffffff
f37122
33a6d7
acd037

Requirements
Must have
• All of what I will say below is suggestive (I’m not a design expert), and I’m open to divert from it, if it makes sense and feels more interesting.
• I thought initially of a 2-page flyer (please see draft flyer attached). The first page could help people grasp the essence of the event quickly (in 1 or 2 minutes), and then, if they are interested/motivated, they would continue reading through page 2, which has more info about the Program in itself.
• Potential Structure
• Page 1
• . About the Information Session on the Tranquil Venture Course
• . Visible Date & Time, Contacts, Venue (and other relevant info)
• . About me (the facilitator)
• Page 2
• . About the Tranquil Venture Course
• I include a Powerpoint draft of the flyer with the content. The design is rudimentary and precarious from an aesthetics/organization point of view, and this is mainly where I need help (and maybe in other aspects too!).
• On the flyer, I would like to include:
• . A photo of myself (I attach 1 picture).
• . 1 or 2 beautiful-nature photos (cropped or full). One may have to do with looking at the sky, dreaming, and imagining a new work and life (2 photos with sky and clouds attached). The other has to do with walking the transformation journey (the photo with the person walking through the forest path).
• . brightfold joy logo or logos (there are two slightly different ones, that can be used for different purposes). For the first page, I would like the brightfold joy logo that has "brightfold joy" written on the bottom, with the saying "Stillness, Craft and Venture for Joy" beneath. This is the main logo. For the 2nd page, you can choose the logo that adapts better.
• - Where it says the "the way out is in" it would be great to have a similar font to the one I attach (see file "Font_the_way_out_is_in.png" and Ankecallig-fg.ttf
Nice to have
• In terms of colours, I would not divert much from the logo colours (and of course white and black). I would like the flyer to be quite white. Almost like fairy-tale white: the white horse, the white snow, the white of the stars, the white heaven. White could be the base colour. White means peace, tranquillity, calm contentment, a smile.
• And then use the other colours. The green of the mindfulness. The blue of the sky, the dreams. And the orange of the sun, the energy, the fire, the action. And maybe the black for text.
• Where it says the "the way out is in" it would be great to have a similar font to the one I attach (see file "Font_the_way_out_is_in".
• I would like this flyer to be a piece of art, in every possible way. Simple, beautiful, ease, light, peaceful, calm happy. Just like the Tranquil Venture Course and brightfold joy Company that I am creating intends to be. The mission of this Program and Company is to be a designer, a painter (a Picasso) of happier and more fulfilling human lives.
• I am very much looking forward to seeing your proposal(s).

```html
<!DOCTYPE html>
<html lang="en">
<head>
<meta charset="utf-8">
<title>Tranquil Venture Course – Information Session Flyer</title>
<link href="https://fonts.googleapis.com/css2?family=Open+Sans:wght@700;800&family=Lato:wght@400;700;900&family=Oswald:wght@600&family=Tinos&display=swap" rel="stylesheet">
<style>
  :root{
    --white:#ffffff;
    --orange:#f37122;
    --orange-title:#ef7d2c;
    --blue:#33a6d7;
    --green:#acd037;
    --green-title:#8cc63f;
    --ink:#1d1d1d;
    --deep-green:#1f4d1a;
    --stage:#3b3b3b;
    --mist:#eceeec;
  }
  *{box-sizing:border-box;margin:0;padding:0}
  html,body{width:1200px;height:900px;overflow:hidden;background:var(--stage)}
  body{position:relative;font-family:"Lato",sans-serif;color:var(--ink)}

  .page{position:absolute;top:75px;height:713px;background:var(--white);overflow:hidden;box-shadow:0 4px 16px rgba(0,0,0,.35)}
  .page--front{left:71px;width:477px}
  .page--back{left:623px;width:505px}
  .abs{position:absolute}
  .center{left:0;right:0;text-align:center}

  .pill{position:absolute;height:22px;border-radius:11px;color:var(--white);font-weight:700;font-size:14px;line-height:22px;text-align:center}
  .pill--blue{background:var(--blue)}
  .pill--orange{background:var(--orange)}

  /* front page */
  .mist{left:0;right:0;top:500px;bottom:0;background:linear-gradient(180deg,rgba(255,255,255,0) 0%,var(--mist) 45%,#e2e5e2 100%)}
  .front-title{top:38px;font-family:"Open Sans",sans-serif;font-weight:800;font-size:68px;line-height:1;color:var(--orange-title);letter-spacing:1px}
  .front-subtitle{top:108px;font-size:30px;line-height:1.1}
  .date-band{top:157px;left:0;right:0;height:33px;background:var(--green);color:var(--white);font-size:20px;font-weight:700;line-height:33px;text-align:center}
  .venue{top:201px;font-size:14px;font-weight:700}
  .lead{font-size:9px;font-weight:700;color:var(--deep-green);line-height:1.35;left:26px;right:26px;text-align:center}
  .facilitator-name{top:416px;font-size:14px;font-weight:700;white-space:nowrap}
  .portrait{left:57px;top:457px;width:134px;height:144px}
  .bio{left:198px;top:460px;width:275px;font-size:9px;line-height:1.32;text-align:justify}
  .footer-tab{left:0;bottom:0;width:477px;height:72px}
  .tel{left:32px;top:655px;font-family:"Oswald",sans-serif;font-weight:600;font-size:18px;line-height:1}
  .booking{left:32px;top:677px;width:200px;font-size:9px;line-height:1.2}
  .brand{left:285px;top:627px;display:flex;align-items:center;gap:10px}
  .brand-mark{width:50px;height:50px;border-radius:50%;background:var(--orange)}
  .brand-name{font-size:23px;line-height:.95;color:var(--blue);font-weight:400}
  .web{right:20px;top:693px;font-size:9px;font-weight:700;letter-spacing:1.3px;color:var(--ink)}

  /* back page */
  .back-title{top:38px;font-family:"Open Sans",sans-serif;font-weight:800;font-size:40px;line-height:1;color:var(--green-title)}
  .back-subtitle{top:72px;font-size:34px;line-height:1.1}
  .intro{left:14px;right:14px;top:127px;font-size:9px;line-height:1.35;text-align:center}
  .cycle{left:72px;top:200px;width:180px;height:130px}
  .about-text{left:249px;top:207px;width:234px;font-size:9px;line-height:1.32;text-align:justify}
  .program-text{left:25px;top:363px;width:215px;font-size:9px;line-height:1.32;text-align:justify}
  .outcomes{left:262px;top:364px;width:212px;list-style:none;font-size:9px;line-height:1.3}
  .outcomes li,.diffs li{position:relative;padding-left:18px;margin-bottom:6px}
  .outcomes li::before,.diffs li::before{content:"";position:absolute;left:2px;top:2px;width:9px;height:9px;border-radius:50%;background:var(--blue)}
  .diff-intro{top:483px;font-size:9.5px;font-weight:700}
  .diffs{list-style:none;font-size:9px;line-height:1.3;top:509px;width:212px}
  .diffs li{margin-bottom:10px}
  .diffs--left{left:32px}
  .diffs--right{left:265px}
  .divider{left:258px;top:509px;width:1px;height:58px;background:#9a9a9a}
  .format{left:40px;right:40px;top:587px;font-size:9.5px;font-weight:700;line-height:1.35;text-align:center}
  .motto-band{left:0;right:0;top:628px;height:32px;background:var(--green);font-family:"Tinos",serif;font-size:16px;line-height:32px;text-align:center;letter-spacing:.5px}
  .footer-info{top:673px;font-size:8px;font-weight:700;line-height:1.35}
  .footer-info--left{left:47px}
  .footer-info--right{right:34px;text-align:center}
</style>
</head>
<body>

<section class="page page--front">
  <div class="abs mist" role="img" aria-label="Faint misty landscape with sky and open field"></div>

  <h1 class="abs center front-title">TRANQUIL</h1>
  <p class="abs center front-subtitle">Venture Course</p>
  <div class="abs date-band">Thursday 18th July 2019, from 19:30 to 21:00</div>
  <p class="abs center venue">Venue: Lumen Coworking, C/ Olivera 42, Barcelona</p>

  <h2 class="pill pill--blue" style="left:167px;top:237px;width:144px">Information Session</h2>
  <p class="abs lead" style="top:265px">The purpose of this Information Session is to give you a real insight into the Tranquil Venture Course and how it can help you get the most out of your work and life.</p>

  <h2 class="pill pill--orange" style="left:128px;top:312px;width:250px">How much and who can come?</h2>
  <p class="abs lead" style="top:341px">The purpose of this Information Session is to give you a real insight into the Tranquil Venture Course and how it can help you get the most out of your work and life.</p>

  <h2 class="pill pill--blue" style="left:194px;top:385px;width:118px">Facilitator</h2>
  <p class="abs center facilitator-name">Dr Marco Lindqvist, Visiting Research Fellow, University of Harrowmere</p>

  <svg class="abs portrait" viewBox="0 0 134 144" role="img" aria-label="Portrait photo of the facilitator">
    <defs>
      <linearGradient id="portraitTone" x1="0" y1="0" x2="0" y2="1">
        <stop offset="0" stop-color="#dcdfe3"/>
        <stop offset="1" stop-color="#5b6470"/>
      </linearGradient>
    </defs>
    <ellipse cx="67" cy="72" rx="64" ry="69" fill="url(#portraitTone)" stroke="#acd037" stroke-width="4"/>
  </svg>

  <p class="abs bio">Marco joined the University of Harrowmere (School of Management) as a Lecturer in Venture Studies in 2015. He completed his PhD in Venture Studies at Kelvinbrook Business School (University of Kelvinbrook) in 2014. His dissertation received the Alder Doctoral Dissertation Award from the Society of Management Studies. Marco began his working career in the semiconductor industry as a production engineer (Semivolt), and then in healthcare as a sales engineer (Meditrane). After his MBA, he worked as a strategy consultant at Douro Business School. Originally from Portugal, Marco enjoys designing and launching new ideas, international communities, mindfulness retreats, and musical improvisation.</p>

  <svg class="abs footer-tab" viewBox="0 0 477 72" aria-hidden="true">
    <path d="M0 2 H200 C235 2 245 40 280 40 H477 V72 H0 Z" fill="#acd037"/>
  </svg>
  <p class="abs tel">Tel: +34 600 555 214</p>
  <p class="abs booking">Information &amp; Booking: Please contact for more information or to book a place</p>

  <div class="abs brand">
    <span class="brand-mark"></span>
    <span class="brand-name">brightfold<br>joy</span>
  </div>
  <p class="abs web">www.brightfoldjoy.example/marco</p>
</section>

<section class="page page--back">
  <div class="abs mist" style="top:440px" role="img" aria-label="Faint misty landscape with sky and open field"></div>

  <h1 class="abs center back-title">WHAT IS TRANQUIL</h1>
  <p class="abs center back-subtitle">Venture</p>
  <p class="abs intro">Being mindful means being aware and awake. Venture is the creation of a new form of organising. Tranquil Venture is then the process of creating or redesigning your work and life with awareness, in a way that is reflective of you, of your passions and values, thus conducing to a greater sense of fulfilment and happiness.</p>

  <h2 class="pill pill--orange" style="left:99px;top:170px;width:306px">What is Tranquil Venture</h2>

  <svg class="abs cycle" viewBox="0 0 180 130" role="img" aria-label="Cycle of four workshops: Insight, Design, Execute, Present, linked by weekly peer support meetings">
    <g fill="none" stroke="#7fb3d5" stroke-width="1.5">
      <path d="M100 22 Q125 28 130 45"/>
      <path d="M128 88 Q122 105 103 110"/>
      <path d="M58 108 Q40 102 36 86"/>
      <path d="M38 45 Q45 28 60 22"/>
    </g>
    <circle cx="80" cy="25" r="23" fill="#8cc63f"/>
    <circle cx="120" cy="63" r="23" fill="#3d8fcf"/>
    <circle cx="82" cy="100" r="23" fill="#f08a3a"/>
    <circle cx="42" cy="63" r="23" fill="#c9c9c9"/>
    <g font-family="Lato, sans-serif" font-size="4.6" fill="#ffffff" text-anchor="middle" font-weight="700">
      <text x="80" y="21">Workshop 1</text><text x="80" y="27">-INSIGHT-</text><text x="80" y="33">(5 hours)</text>
      <text x="120" y="59">Workshop 2</text><text x="120" y="65">-DESIGN-</text><text x="120" y="71">(5 hours)</text>
      <text x="82" y="96">Workshop 3</text><text x="82" y="102">-EXECUTE-</text><text x="82" y="108">(5 hours)</text>
      <text x="42" y="59">Workshop 4</text><text x="42" y="65">-PRESENT-</text><text x="42" y="71">(5 hours)</text>
    </g>
    <g font-family="Lato, sans-serif" font-size="4.2" fill="#555555">
      <text x="112" y="18">Weekly Peer Support</text><text x="112" y="23">(WPS) meetings</text>
      <text x="20" y="22">WPS meetings</text>
      <text x="135" y="106">WPS meetings</text>
      <text x="10" y="112">WPS meetings</text>
    </g>
  </svg>

  <p class="abs about-text">The Tranquil Venture Course is a 4-month long transformative journey for people who feel stuck or not entirely satisfied with their work and/or life. It will be of benefit for everyone, at any stage. The Program consists of a series of four 5-hour workshops, one per month, complemented by 2-hour weekly peer support meetings. It combines mindfulness techniques, design thinking methodology and venture frameworks to achieve the desired</p>

  <h2 class="pill pill--blue" style="left:165px;top:330px;width:175px">The Program</h2>
  <p class="abs program-text">Many people are not entirely satisfied with their work, but they don't know what to do about it. The Tranquil Venture Course offers an opportunity, a safe place, a collective journey to help you reflect, design, and (very likely) do something about it. By the end of the Program, you should have:</p>
  <ul class="abs outcomes">
    <li>Increased awareness, clarity and confidence</li>
    <li>A deeper insight on what makes you happier and what you want</li>
    <li>A clear design integrating your intended work and life Initiated the execution of this design.</li>
  </ul>

  <h2 class="pill pill--orange" style="left:195px;top:446px;width:112px">Why</h2>
  <p class="abs center diff-intro">This Program differs from existing venture programs in many ways:</p>
  <ul class="abs diffs diffs--left">
    <li>It starts upstream with mindfulness and self analysis to look deeply into yourself</li>
    <li>Design and execution decisions are rooted on happiness rather than (only) financials</li>
  </ul>
  <div class="abs divider"></div>
  <ul class="abs diffs diffs--right">
    <li>The process is holistic and inclusive, aiming at designing an integrated work and life, and on building synergies between your different parts.</li>
  </ul>
  <p class="abs format">The Program format includes lectures, individual work, group sharing, guided activities, experiential exercises, video, audio, handouts and other resources.</p>

  <div class="abs motto-band">THE WAY OUT IS IN</div>
  <p class="abs footer-info footer-info--left">Date: Thursday 23th, from 19:30 to 21:00<br>Venue: Lumen Coworking, C/ Olivera 42, Barcelona</p>
  <p class="abs footer-info footer-info--right">Email: info@brightfoldjoy.example<br>Tel: +34 600 555 214 (video call and chat)</p>
</section>

</body>
</html>
```